Patient Report Folder for modern Chiropractic Clinic

We are looking for someone to design a patient folder and 3 simple info sheets to go along with it.

The design should be clean and masculine with an artsy touch. I am a fan of the Fra Mollego style drawings so would like the background to be a style of parchment paper. The info sheets should follow a similar style.

Please check the “Design Outline” pdf and the “Folder Design” file before getting started. The 3 info sheets are going to be placed in the pocket where “Attachment #3” will be.

- The format should be DIN A4 according to the printing details attached in the files section. Please see the ''Folder Design.jpg'' for the design of the folder.
- All the designs should be different and unique in nature but match each other.
- The text for Info Sheet #3 can be left blank.

It is probably best to take a look at the ''Design Outline'' file first to see how I envision the design to be. Please do not hesitate to ask me questions or to discuss ideas.

Target Market(s)

upper class audience with a focus on health and well-being

Industry/Entity Type

Chiropractic // Health

Requirements
Must have
• The colours should be fitting with the main colours in the logo: #1ccad5 and #b1b2b4
Nice to have
• Fra Mollego Style design and the background on parchment paper style. It is not a must but if anyone can come up with a suitable design and colorway that would be great.

```html
<!DOCTYPE html>
<html lang="en">
<head>
<meta charset="utf-8">
<title>Altura 88 – Patient Folder Dieline</title>
<link href="https://fonts.googleapis.com/css2?family=Poppins:wght@400;500;600;700&display=swap" rel="stylesheet">
<style>
  :root {
    --stage-dark: #2b2b2b;
    --stage-mid: #383838;
    --folder-tan: #cfa96b;
    --ink-brown: #7a5520;
    --ink-dark: #222222;
    --cut-line: #2db34a;
    --fold-mark: #555555;
    --field-white: #ffffff;
  }
  html, body {
    margin: 0;
    padding: 0;
    width: 1200px;
    height: 1200px;
    overflow: hidden;
  }
  .stage {
    position: relative;
    width: 1200px;
    height: 1200px;
    background: linear-gradient(90deg, var(--stage-dark) 0%, var(--stage-mid) 50%, var(--stage-dark) 100%);
    font-family: "Poppins", sans-serif;
  }
  .dieline {
    position: absolute;
    inset: 0;
  }
  .quote {
    position: absolute;
    left: 200px;
    top: 364px;
    width: 326px;
    text-align: center;
    color: var(--ink-brown);
    font-size: 12.5px;
    letter-spacing: 3.6px;
    line-height: 20px;
  }
  .brand {
    position: absolute;
    left: 760px;
    top: 470px;
    width: 290px;
    text-align: center;
    color: var(--ink-brown);
    font-weight: 600;
    font-size: 40px;
    letter-spacing: 2px;
    line-height: 50px;
  }
  .patient-label {
    position: absolute;
    left: 774px;
    top: 695px;
    width: 261px;
    text-align: center;
    color: var(--ink-brown);
    font-weight: 600;
    font-size: 11px;
    letter-spacing: 3.2px;
  }
  .patient-field {
    position: absolute;
    left: 774px;
    top: 717px;
    width: 261px;
    height: 30px;
    background: var(--field-white);
  }
  .contact {
    position: absolute;
    left: 126px;
    top: 708px;
    height: 53px;
    border-left: 1px solid var(--ink-brown);
    padding-left: 32px;
    color: var(--ink-dark);
    font-size: 10px;
    line-height: 11.5px;
  }
  .contact-item {
    position: relative;
    margin-bottom: 3.5px;
  }
  .contact-item svg {
    position: absolute;
    left: -14px;
    top: 1px;
    width: 8px;
    height: 8px;
  }
  .pocket-slogan {
    position: absolute;
    left: 140px;
    top: 835px;
    width: 274px;
    text-align: center;
    color: var(--ink-brown);
    font-weight: 500;
    font-size: 10.5px;
    letter-spacing: 3px;
    transform: rotate(180deg);
  }
</style>
</head>
<body>
<div class="stage">
  <svg class="dieline" width="1200" height="1200" viewBox="0 0 1200 1200">
    <path d="M88.8 39.7 H1172.6 V798 H616.7 V900.5 Q621 956 577.6 972 L88.8 1159 V798 H76.4 L27.9 776.3 V462.7 L76.4 449 H88.8 Z"
          fill="var(--folder-tan)" stroke="var(--cut-line)" stroke-width="1"/>
    <line x1="623.5" y1="376" x2="623.5" y2="442" stroke="var(--fold-mark)" stroke-width="1.2"/>
    <line x1="638.4" y1="376" x2="638.4" y2="442" stroke="var(--fold-mark)" stroke-width="1.2"/>
    <circle cx="898" cy="391" r="70" fill="none" stroke="var(--ink-brown)" stroke-width="2.5"/>
  </svg>

  <div class="quote">
    THE GREATEST WEALTH IS HEALTH<br>- ORLEN VASH -
  </div>

  <div class="brand">ALTURA 88</div>

  <div class="patient-label">PATIENT’S NAME</div>
  <div class="patient-field"></div>

  <div class="contact">
    <div class="contact-item">
      <svg viewBox="0 0 10 10"><path d="M5 9.5 C2.5 6.5 1.5 5 1.5 3.6 A3.5 3.5 0 0 1 8.5 3.6 C8.5 5 7.5 6.5 5 9.5Z" fill="none" stroke="var(--ink-brown)" stroke-width="1.2"/><circle cx="5" cy="3.6" r="1.2" fill="var(--ink-brown)"/></svg>
      Lindenhof Weg 12,<br>71034 Feldbrunn-Ostheim
    </div>
    <div class="contact-item">
      <svg viewBox="0 0 10 10"><rect x="1" y="2" width="8" height="6" fill="none" stroke="var(--ink-brown)" stroke-width="1.2"/><path d="M1 2 L5 5.5 L9 2" fill="none" stroke="var(--ink-brown)" stroke-width="1.2"/></svg>
      info@altura88praxis.de
    </div>
    <div class="contact-item">
      <svg viewBox="0 0 10 10"><circle cx="5" cy="5" r="4" fill="none" stroke="var(--ink-brown)" stroke-width="1.1"/><ellipse cx="5" cy="5" rx="1.8" ry="4" fill="none" stroke="var(--ink-brown)" stroke-width="0.9"/><line x1="1" y1="5" x2="9" y2="5" stroke="var(--ink-brown)" stroke-width="0.9"/></svg>
      altura88praxis.de
    </div>
  </div>

  <div class="pocket-slogan">LEAVE YOUR WORRIES BEHIND...</div>
</div>
</body>
</html>
```